We would like a business card that includes our logo on the front and the following information on the back:

Marcus Keene, Owner
Phone: (555) 614-8027
email: mkeenefencing@postvale.net

Marty Keene & Sons Fencing provides the following services:
Barbed wire
Smooth wire
High tensile
Electric

On the bottom of the card please add:
Please call or email Marcus for estimates.

```html
<!DOCTYPE html>
<html lang="en">
<head>
<meta charset="utf-8">
<title>Marty Keene &amp; Sons Fencing – Business Card</title>
<link rel="stylesheet" href="https://fonts.googleapis.com/css2?family=Arimo:wght@400;700&display=swap">
<style>
  :root {
    --backdrop: #e4e3e1;
    --card: #ffffff;
    --brown: #7a5238;
    --ink: #2b2522;
    --grey: #6f6f6f;
    --rule: #3a3330;
    --faint: #e6e6e6;
  }
  * { box-sizing: border-box; margin: 0; padding: 0; }
  html, body { width: 1200px; height: 802px; overflow: hidden; }
  body {
    background: var(--backdrop);
    font-family: "Arimo", Arial, sans-serif;
    color: var(--ink);
    position: relative;
  }
  .card {
    position: absolute;
    top: 246px;
    width: 540px;
    height: 309px;
    background: var(--card);
    box-shadow: 0 6px 18px rgba(0,0,0,0.12);
    overflow: hidden;
  }
  .card--contact { left: 40px; }
  .card--services { left: 620px; }

  /* contact side */
  .fence-backdrop {
    position: absolute;
    right: 0; top: 84px;
    width: 180px; height: 225px;
    background: linear-gradient(160deg, #eeeeee 0%, var(--faint) 60%, #f4f4f4 100%);
  }
  .owner {
    position: absolute;
    right: 36px; top: 28px;
    text-align: right;
  }
  .owner__name {
    font-weight: 700;
    font-size: 19px;
    color: var(--brown);
    letter-spacing: 0.3px;
  }
  .owner__title {
    font-size: 13px;
    color: var(--grey);
    margin-top: 2px;
  }
  .brand {
    position: absolute;
    display: flex;
    flex-direction: column;
    align-items: center;
  }
  .brand__mark {
    width: 14px; height: 14px;
    background: var(--brown);
    margin-bottom: 10px;
  }
  .brand__name {
    font-weight: 700;
    color: var(--ink);
    text-align: center;
    line-height: 1.25;
    letter-spacing: 1px;
    text-transform: uppercase;
  }
  .card--contact .brand { left: 36px; top: 108px; width: 250px; }
  .card--contact .brand__name { font-size: 17px; }
  .card--contact .brand__rule {
    width: 230px; height: 1px; background: var(--rule); margin-top: 10px;
  }
  .contact {
    position: absolute;
    left: 36px; bottom: 30px;
    list-style: none;
    font-size: 14px;
    color: var(--grey);
  }
  .contact li { display: flex; align-items: center; gap: 9px; margin-top: 6px; }
  .contact svg { width: 14px; height: 14px; fill: var(--brown); flex: none; }

  /* services side */
  .card--services .brand { left: 0; right: 0; top: 44px; }
  .card--services .brand__name { font-size: 24px; }
  .card--services .brand__rule {
    width: 330px; height: 1px; background: var(--rule); margin-top: 12px;
  }
  .services {
    position: absolute;
    left: 0; right: 0; top: 178px;
    text-align: center;
  }
  .services__heading {
    font-weight: 700;
    font-size: 16px;
    color: var(--brown);
    margin-bottom: 10px;
  }
  .services__list {
    list-style: none;
    display: flex;
    flex-wrap: wrap;
    justify-content: center;
    gap: 6px 22px;
    font-size: 15px;
    color: var(--ink);
    padding: 0 40px;
  }
  .services__list li::before {
    content: "";
    display: inline-block;
    width: 5px; height: 5px;
    border-radius: 50%;
    background: var(--brown);
    margin-right: 8px;
    vertical-align: middle;
  }
  .estimate-note {
    position: absolute;
    left: 0; right: 0; bottom: 26px;
    text-align: center;
    font-size: 13px;
    color: var(--grey);
  }
</style>
</head>
<body>

<section class="card card--contact">
  <div class="fence-backdrop" role="img" aria-label="Faint grey fence post decoration"></div>
  <div class="owner">
    <p class="owner__name">MARCUS KEENE</p>
    <p class="owner__title">Owner</p>
  </div>
  <div class="brand">
    <span class="brand__mark"></span>
    <p class="brand__name">Marty Keene &amp; Sons<br>Fencing</p>
    <span class="brand__rule"></span>
  </div>
  <ul class="contact">
    <li>
      <svg viewBox="0 0 24 24" aria-hidden="true"><path d="M6.6 10.8a15.1 15.1 0 0 0 6.6 6.6l2.2-2.2a1 1 0 0 1 1-.25 11.4 11.4 0 0 0 3.6.57 1 1 0 0 1 1 1V20a1 1 0 0 1-1 1A17 17 0 0 1 3 4a1 1 0 0 1 1-1h3.5a1 1 0 0 1 1 1c0 1.25.2 2.45.57 3.57a1 1 0 0 1-.25 1z"/></svg>
      (555) 614-8027
    </li>
    <li>
      <svg viewBox="0 0 24 24" aria-hidden="true"><path d="M2 5h20v14H2z M3.5 6.5 12 13l8.5-6.5" /></svg>
      mkeenefencing@postvale.net
    </li>
  </ul>
</section>

<section class="card card--services">
  <div class="brand">
    <span class="brand__mark"></span>
    <p class="brand__name">Marty Keene &amp; Sons<br>Fencing</p>
    <span class="brand__rule"></span>
  </div>
  <div class="services">
    <p class="services__heading">SERVICES:</p>
    <ul class="services__list">
      <li>Barbed wire</li>
      <li>Smooth wire</li>
      <li>High tensile</li>
      <li>Electric</li>
    </ul>
  </div>
  <p class="estimate-note">Please call or email Marcus for estimates.</p>
</section>

</body>
</html>
```